Social Media Overlay for Ormond Real Estate

We need an social media overlay that can be added to a photo of a house that includes our current logo and a call to action of "Just Listed". This needs to be something that we can use for every new house that we list. Attached is our current logo in both company colors, purple and white. An example of a overlay from Plazeo that we like.

Target Market(s)

Social Media Real Estate Community - Real Estate Agents, Brokers, Buyers & Sellers

Industry/Entity Type

Real Estate

Font styles to use
Sans Serif

Colors
6c459b

Requirements
Must have
• the company colors, purple and white and the company logo
Nice to have
• call to action "Just Listed"
• some layered, texture, or 3-D effect
Should not have
• Should be clean and simple; nothing too busy

```html
<!DOCTYPE html>
<html lang="en">
<head>
<meta charset="utf-8">
<title>Ormond Real Estate – Just Listed Overlay</title>
<link rel="stylesheet" href="https://fonts.googleapis.com/css2?family=Poppins:wght@500;600&display=swap">
<style>
  :root {
    --brand-purple: #6c459b;
    --brand-purple-deep: #5a2f8c;
    --button-purple: #7a1fc9;
    --button-purple-light: #b266f0;
    --accent-yellow: #f6b400;
    --white: #ffffff;
    --sky: #3d86d6;
    --foliage: #3f6a4c;
    --lawn: #4d6a38;
  }
  * { margin: 0; padding: 0; box-sizing: border-box; }
  html, body {
    width: 1200px;
    height: 642px;
    overflow: hidden;
    background: var(--white);
  }
  .overlay {
    position: relative;
    width: 1200px;
    height: 642px;
    background: var(--white);
    font-family: "Poppins", sans-serif;
  }
  .listing-photo {
    position: absolute;
    left: 198px;
    top: 0;
    width: 1002px;
    height: 642px;
    background:
      linear-gradient(180deg, rgba(108,69,155,0) 40%, rgba(108,69,155,0.25) 100%),
      linear-gradient(180deg, var(--sky) 0%, #5e8fb5 18%, var(--foliage) 38%, #7b8a86 55%, #5d6a55 72%, var(--lawn) 85%, #3f5a30 100%);
  }
  .side-band {
    position: absolute;
    left: 0;
    top: 47px;
    width: 198px;
    height: 595px;
    background: var(--brand-purple);
  }
  .accent-line {
    position: absolute;
    left: 43px;
    top: 602px;
    width: 275px;
    height: 7px;
    background: var(--accent-yellow);
  }
  .corner-frame {
    position: absolute;
    left: 889px;
    top: 42px;
    width: 276px;
    height: 282px;
    border-top: 4px solid var(--white);
    border-right: 4px solid var(--white);
  }
  .brand-panel {
    position: absolute;
    left: 896px;
    top: 339px;
    width: 267px;
    height: 136px;
    background: rgba(255,255,255,0.85);
    display: flex;
    align-items: center;
    justify-content: center;
    gap: 10px;
  }
  .brand-mark {
    width: 14px;
    height: 14px;
    background: var(--brand-purple-deep);
    flex: none;
  }
  .brand-name {
    color: var(--brand-purple-deep);
    font-weight: 600;
    font-size: 21px;
    line-height: 1;
    white-space: nowrap;
  }
  .cta {
    position: absolute;
    left: 892px;
    top: 527px;
    width: 273px;
    height: 54px;
    border-radius: 27px;
    border: 3px solid #d8b8f5;
    background: linear-gradient(180deg, var(--button-purple-light) 0%, var(--button-purple) 50%, #5f12a8 100%);
    color: var(--white);
    font-weight: 600;
    font-size: 25px;
    letter-spacing: 0.5px;
    display: flex;
    align-items: center;
    justify-content: center;
    box-shadow: 0 2px 6px rgba(0,0,0,0.3);
  }
  .cta-reflection {
    position: absolute;
    left: 892px;
    top: 584px;
    width: 273px;
    height: 40px;
    border-radius: 0 0 27px 27px;
    background: linear-gradient(180deg, rgba(122,31,201,0.55) 0%, rgba(122,31,201,0) 100%);
  }
</style>
</head>
<body>
  <div class="overlay">
    <div class="listing-photo" role="img" aria-label="Photo of a newly listed two-storey craftsman house with stone pillars, tall evergreen trees and a green front lawn under a blue sky"></div>
    <div class="side-band"></div>
    <div class="accent-line"></div>
    <div class="corner-frame"></div>
    <div class="brand-panel">
      <span class="brand-mark"></span>
      <span class="brand-name">Ormond Real Estate</span>
    </div>
    <div class="cta-reflection"></div>
    <div class="cta">JUST LISTED</div>
  </div>
</body>
</html>
```